Ridgeline Sawcutting, Inc. Business Card

Create a business card that is eye catching and based around concrete sawcutting. I've attached our current business card and logo for reference. We like aspects of the current business card, but it is starting to feel very loud and lost. We would like something that is still fun but is more modern and streamlined.

```html
<!DOCTYPE html>
<html lang="en">
<head>
<meta charset="utf-8">
<title>Ridgeline Sawcutting, Inc. Business Card</title>
<link href="https://fonts.googleapis.com/css2?family=Montserrat:wght@400;500;700&display=swap" rel="stylesheet">
<style>
  :root {
    --page: #e9e9ea;
    --card-black: #141414;
    --card-grey: #a9aaac;
    --white: #ffffff;
    --red: #d3202c;
    --navy: #1f2a6b;
    --ink: #1b1b1b;
  }
  * { box-sizing: border-box; margin: 0; padding: 0; }
  html, body { width: 1200px; height: 786px; overflow: hidden; }
  body {
    background: var(--page);
    font-family: "Montserrat", sans-serif;
    position: relative;
  }
  .card {
    position: absolute;
    top: 244px;
    width: 520px;
    height: 298px;
    overflow: hidden;
    box-shadow: 0 10px 28px rgba(0,0,0,0.22);
  }
  /* Front */
  .card-front { left: 50px; background: var(--card-black); color: var(--white); }
  .front-circle {
    position: absolute;
    left: 262px; top: -70px;
    width: 330px; height: 330px;
    border-radius: 50%;
    background: var(--white);
  }
  .front-brand {
    position: absolute;
    left: 300px; top: 100px;
    width: 200px;
    text-align: center;
    color: var(--navy);
    font-weight: 700;
    font-size: 21px;
    line-height: 1.2;
    letter-spacing: 1px;
    text-transform: uppercase;
  }
  .holder-name {
    position: absolute; left: 34px; top: 110px;
    color: var(--red); font-weight: 700; font-size: 21px;
  }
  .address {
    position: absolute; left: 34px; top: 160px;
    font-size: 13px; line-height: 1.35;
  }
  .contact-list {
    position: absolute; left: 34px; top: 206px;
    list-style: none; font-size: 13px;
  }
  .contact-list li { display: flex; align-items: center; gap: 12px; height: 20px; }
  .contact-list svg { width: 14px; height: 14px; fill: var(--red); flex: none; }
  /* Back */
  .card-back { left: 630px; background: var(--card-grey); }
  .back-brand {
    position: absolute; left: 0; right: 0; top: 58px;
    display: flex; align-items: center; justify-content: center; gap: 10px;
    color: var(--navy); font-weight: 700; font-size: 22px;
    letter-spacing: 1px; text-transform: uppercase;
  }
  .back-brand .dot { width: 14px; height: 14px; border-radius: 50%; background: var(--navy); }
  .services-title {
    position: absolute; left: 0; right: 0; top: 168px;
    text-align: center; color: var(--red);
    font-weight: 700; font-size: 15px; letter-spacing: 0.5px;
  }
  .services-rule {
    position: absolute; left: 205px; width: 110px; top: 192px;
    height: 1.5px; background: var(--ink);
  }
  .services-list {
    position: absolute; left: 0; right: 0; top: 226px;
    list-style: none; display: flex; justify-content: center; gap: 14px;
    font-size: 10.5px; color: var(--ink); text-transform: uppercase;
  }
  .services-list li::before {
    content: ""; display: inline-block; width: 5px; height: 5px;
    border-radius: 50%; background: var(--red); margin-right: 6px;
    vertical-align: middle;
  }
</style>
</head>
<body>
  <section class="card card-front">
    <div class="front-circle"></div>
    <div class="front-brand">Ridgeline Sawcutting</div>
    <h1 class="holder-name">Dana Moretti</h1>
    <p class="address">48 Alder Row<br>Westbrook, NJ 07610</p>
    <ul class="contact-list">
      <li><svg viewBox="0 0 16 16"><path d="M3 1l3 3-1.5 2c1 2 3 4 5 5L11.5 9.5l3 3-2 2.5C7 14 2 9 1 3z"/></svg>855-RL CUTS</li>
      <li><svg viewBox="0 0 16 16"><path d="M1 5c2-3 12-3 14 0v2h-4V5H5v2H1zM3 8h10l1 6H2z"/></svg>855. 555. 0142</li>
      <li><svg viewBox="0 0 16 16"><path d="M4 0h8v16H4zM5.5 2v10h5V2z"/></svg>973. 555. 0178</li>
      <li><svg viewBox="0 0 16 16"><path d="M0 3h16v1L8 9 0 4zM0 6l8 5 8-5v7H0z"/></svg>dana@ridgelinesawcutting</li>
    </ul>
  </section>

  <section class="card card-back">
    <div class="back-brand"><span class="dot"></span>Ridgeline Sawcutting</div>
    <h2 class="services-title">OUR SERVICES</h2>
    <div class="services-rule"></div>
    <ul class="services-list">
      <li>Wall Sawing</li>
      <li>Core Drilling</li>
      <li>Slab Sawing</li>
      <li>Breaking &amp; Removal</li>
    </ul>
  </section>
</body>
</html>
```